Business Card Design Project

We need a business card to reflect the design of our website - just so it all ties in - it has a retro feel and can be found at http://www.lunetaswingduo.com
We will need our phone 0493 215 764
Web address, and email lunetaduo@corvanet.com included
Our catch cry is "Classic Cocktail Music"
Perfect Live Music for Private & Corporate Events, Weddings and Dinner Music
Our names should be included :-
Deborah Feltham / piano & Owen Lockett / bass
I am now also including our logo so that it can be included (in part or whole) somehow in the design
My partner thinks we should include our logo in some form in the design of the card - i will attach this here for you. I will attach eps but if you prefer another format please let me know
Regards
Debbie

```html
<!DOCTYPE html>
<html lang="en">
<head>
<meta charset="utf-8">
<title>Luneta Duo – Business Card</title>
<link rel="stylesheet" href="https://fonts.googleapis.com/css2?family=Federo&family=Ubuntu:wght@400;500;700&family=Ubuntu+Condensed&display=swap">
<style>
  :root{
    --backdrop:#2a2a2a;
    --teal:#8cc0bf;
    --teal-deep:#79aeae;
    --coral:#d9825f;
    --cream:#ece6d3;
    --stone:#d5d0bf;
    --charcoal:#3a3a3a;
    --ink:#2f2f2f;
    --orange:#e0562b;
    --white:#ffffff;
  }
  *{box-sizing:border-box;margin:0;padding:0}
  html,body{width:1200px;height:900px;overflow:hidden;background:var(--backdrop)}
  .canvas{position:relative;width:1200px;height:900px}

  .card{position:absolute;top:290px;width:560px;height:320px;overflow:hidden;box-shadow:0 12px 30px rgba(0,0,0,.45)}
  .card--front{left:27px;background:var(--teal)}
  .card--back{left:613px;background:var(--charcoal)}

  /* front */
  .front-stitch{position:absolute;left:0;top:0;width:560px;height:90px}
  .front-seal{position:absolute;left:255px;top:22px;width:50px;height:50px;border-radius:50%;background:var(--ink);border:3px solid var(--cream)}
  .instrument{position:absolute;background:linear-gradient(160deg,#fbfaf5,#e4e8e6);border-radius:40% 40% 30% 30%}
  .instrument--left{left:30px;top:40px;width:70px;height:120px}
  .instrument--right{left:440px;top:160px;width:70px;height:105px}
  .brand-name{position:absolute;left:0;right:0;top:92px;text-align:center;font-family:"Federo",sans-serif;font-size:58px;letter-spacing:2px;color:var(--cream);line-height:1}
  .tagline{position:absolute;left:170px;top:178px;width:220px;height:28px;background:var(--cream);color:var(--ink);font-family:"Ubuntu Condensed",sans-serif;font-size:13px;letter-spacing:1px;text-align:center;line-height:28px;text-transform:uppercase}
  .tagline::before,.tagline::after{content:"";position:absolute;top:6px;width:18px;height:22px;background:#cfc7ae;z-index:-1}
  .tagline::before{left:-12px}
  .tagline::after{right:-12px}
  .dotted{position:absolute;top:192px;height:0;border-top:2px dotted var(--cream)}
  .dotted--left{left:110px;width:50px}
  .dotted--right{left:400px;width:40px}
  .names-band{position:absolute;left:0;bottom:0;width:100%;height:52px;background:var(--coral);color:var(--white);font-family:"Ubuntu",sans-serif;font-weight:500;font-size:18px;line-height:52px;padding-left:26px}

  /* back */
  .back-top{position:absolute;left:0;top:0;width:100%;height:118px;background:var(--stone)}
  .back-stitch{position:absolute;left:12px;right:12px;top:118px;border-top:1px dashed rgba(255,255,255,.25)}
  .back-bottom{position:absolute;left:0;bottom:0;width:100%;height:38px;background:var(--teal)}
  .back-bottom::before{content:"";position:absolute;left:12px;right:12px;top:7px;border-top:1px dashed rgba(255,255,255,.5)}
  .services{position:absolute;left:40px;right:40px;top:14px;display:flex;justify-content:space-between}
  .service{width:100px;text-align:center;font-family:"Ubuntu Condensed",sans-serif;color:var(--ink);text-transform:uppercase}
  .service__title{font-size:12px;font-weight:700;line-height:1}
  .service__note{font-size:7px;line-height:1.15;height:18px;margin-top:2px}
  .service__icon{display:block;margin:4px auto 0;width:46px;height:46px}
  .service__rule{width:50px;margin:6px auto 0;border-top:2px solid #8a8778}
  .pitch{position:absolute;right:34px;top:148px;text-align:right;font-family:"Ubuntu",sans-serif;color:var(--white)}
  .pitch__lead{color:var(--orange);font-size:20px;font-weight:500}
  .pitch__events{font-size:13px;margin-top:2px}
  .pitch__phone{font-size:24px;font-weight:500;margin-top:8px;letter-spacing:1px}
  .pitch__links{font-size:14px;margin-top:4px}
  .pitch__links em{font-style:normal;color:var(--orange)}
</style>
</head>
<body>
<main class="canvas">

  <section class="card card--front" aria-label="Card front">
    <svg class="front-stitch" viewBox="0 0 560 90" aria-hidden="true">
      <path d="M0 28 H230 Q280 60 330 28 H560" fill="none" stroke="rgba(255,255,255,.45)" stroke-dasharray="3 3"/>
    </svg>
    <div class="front-seal" aria-hidden="true"></div>
    <div class="instrument instrument--left" role="img" aria-label="Illustration of a double bass with piano-key body"></div>
    <h1 class="brand-name">LUNETA DUO</h1>
    <span class="dotted dotted--left"></span>
    <div class="tagline">Classic Cocktail Music</div>
    <span class="dotted dotted--right"></span>
    <div class="instrument instrument--right" role="img" aria-label="Illustration of a double bass with piano-key body"></div>
    <p class="names-band">Deborah Feltham / Piano &amp; Owen Lockett / Bass</p>
  </section>

  <section class="card card--back" aria-label="Card back">
    <div class="back-top"></div>
    <div class="back-stitch"></div>
    <ul class="services">
      <li class="service">
        <div class="service__title">Weddings</div>
        <div class="service__note">Ceremony &amp;<br>Reception</div>
        <svg class="service__icon" viewBox="0 0 46 46" aria-hidden="true"><circle cx="23" cy="23" r="21" fill="var(--orange)" stroke="var(--ink)" stroke-width="2"/><rect x="14" y="15" width="18" height="16" fill="none" stroke="var(--ink)" stroke-width="2"/><path d="M17 15v16M29 15v16" stroke="var(--ink)" stroke-width="1.5"/></svg>
        <div class="service__rule"></div>
      </li>
      <li class="service">
        <div class="service__title">Packages</div>
        <div class="service__note">Cover the whole<br>event</div>
        <svg class="service__icon" viewBox="0 0 46 46" aria-hidden="true"><circle cx="23" cy="23" r="21" fill="var(--orange)" stroke="var(--ink)" stroke-width="2"/><circle cx="23" cy="20" r="7" fill="var(--ink)"/><rect x="19" y="27" width="8" height="6" fill="var(--ink)"/></svg>
        <div class="service__rule"></div>
      </li>
      <li class="service">
        <div class="service__title">Corporate</div>
        <div class="service__note">All events in<br>QLD</div>
        <svg class="service__icon" viewBox="0 0 46 46" aria-hidden="true"><circle cx="23" cy="23" r="21" fill="var(--orange)" stroke="var(--ink)" stroke-width="2"/><path d="M12 22l6-5 10 3 6-3v8l-8 6-8-4-6-1z" fill="var(--ink)"/></svg>
        <div class="service__rule"></div>
      </li>
      <li class="service">
        <div class="service__title">Private</div>
        <div class="service__note">Parties a<br>speciality</div>
        <svg class="service__icon" viewBox="0 0 46 46" aria-hidden="true"><circle cx="23" cy="23" r="21" fill="var(--orange)" stroke="var(--ink)" stroke-width="2"/><ellipse cx="23" cy="23" rx="11" ry="4" fill="none" stroke="var(--ink)" stroke-width="1.5"/><ellipse cx="23" cy="23" rx="11" ry="4" fill="none" stroke="var(--ink)" stroke-width="1.5" transform="rotate(60 23 23)"/><ellipse cx="23" cy="23" rx="11" ry="4" fill="none" stroke="var(--ink)" stroke-width="1.5" transform="rotate(-60 23 23)"/><circle cx="23" cy="23" r="2.5" fill="var(--ink)"/></svg>
        <div class="service__rule"></div>
      </li>
    </ul>
    <div class="pitch">
      <p class="pitch__lead">Perfect Live Music for</p>
      <p class="pitch__events">Private &amp; Corporate Events, Weddings and Dinner Music</p>
      <p class="pitch__phone">0493 215 764</p>
      <p class="pitch__links">lunetaduo@corvanet.com / www.<em>lunetaswingduo</em>.com</p>
    </div>
    <div class="back-bottom"></div>
  </section>

</main>
</body>
</html>
```